INFO and INTEREST Flyer - SEARCH AND RESCUE COMANY

Hello. I would like to create a flyer (preferably 5inch x 7inch) that will serve as the main printed marketing avenue for our SEARCH AND RESCUE company. We are a non profit SEARCH and RESCUE team based out of the MARYLAND area.

We deploy nation wide to help with search and rescue , incident response and disaster relief.

The intention of the flyer is to bring awareness to the community as well as bring in new members and donators. I would like to have a two sided flyer. The first side of the flyer should be geared toward attracting new members. The back side of the flyer should be geared toward getting people to donate to our cause.

Overall I want this to be attractive to many demographics. I don't want it to be too plain. It should engaging while instilling a sense of urgency to our cause.

Target Market(s)

Potential Search and Rescue Members - Potential Donators

Industry/Entity Type

Search And Rescue

Font styles to use
Other font styles liked:
• BOLD and edgy for titles - Normal text for informational areas

Colors

Designer to choose colors to be used in the design.

Requirements
Must have
• I would like to have a two sided flyer. The first side of the flyer should be geared toward attracting new members. The back side of the flyer should be geared toward getting people to donate to our cause.
• I have attached a couple of logo style and file types. The Proper one to be used is the red, white blue round logo with yellow stars.
• Please include our mission statement which is located in red on the "website update" document provided
• Please refer to the attachments I posted . I would like the fonts in the short logo movie to be the same. The main logo for the flyer should have the round corporate logo with the text "Kestrel Ridge Response Unit - Search and Rescue" under it as shown.
Nice to have
• I would like to include some of the pictures form our deployments and vehicles. I would also like to see these be colorful. I like the watercolor colors and textures. Something a little more abstract but i am really open to anything as long as it conveys a good message.
Should not have
• None at this time

```html
<!DOCTYPE html>
<html lang="en">
<head>
<meta charset="utf-8">
<title>Kestrel Ridge Response Unit – Flyer Front and Back</title>
<link rel="stylesheet" href="https://fonts.googleapis.com/css2?family=Bebas+Neue&family=Arimo:wght@400;700&family=Montserrat:wght@800&display=swap">
<style>
:root{
  --stage:#c9c9c9;
  --label:#8e8e8e;
  --navy:#15307a;
  --navy-deep:#0d2466;
  --blue:#2a4aa8;
  --red:#b3121a;
  --red-bright:#d8262b;
  --lime:#b9dc4a;
  --paper:#ffffff;
  --mist:#e9eaee;
  --grey-tab:#9a9ca3;
  --ink:#1b1b1b;
}
*{box-sizing:border-box;margin:0;padding:0}
html,body{width:1200px;height:1200px;overflow:hidden}
body{background:radial-gradient(circle at 55% 45%,#e2e2e2 0%,var(--stage) 75%);position:relative;font-family:"Arimo",Arial,sans-serif;color:var(--ink)}
.side-label{position:absolute;left:155px;font-family:"Montserrat",Arial,sans-serif;font-weight:800;font-size:64px;color:var(--label);transform:translateX(-50%) rotate(-90deg);transform-origin:center;letter-spacing:1px}
.side-label.front{top:264px}
.side-label.back{top:834px}
.card{position:absolute;left:225px;width:751px;height:536px;background:var(--paper);overflow:hidden;box-shadow:0 6px 14px rgba(0,0,0,.25)}
.card.front{top:27px}
.card.back{top:600px}
.abs{position:absolute}
.headline{font-family:"Bebas Neue",Impact,sans-serif;line-height:1;text-align:center;white-space:nowrap}
.top-title{left:0;width:751px;top:14px;font-size:39px;letter-spacing:-.5px}
.front .top-title{color:var(--red)}
.back .top-title{color:var(--navy)}
.band{left:0;top:55px;width:751px;height:230px}
.photo{position:absolute}
.badge-seal{left:296px;top:72px;width:126px;height:126px;border-radius:50%;background:var(--paper);border:5px solid var(--navy);display:flex;align-items:center;justify-content:center;text-align:center;font-family:"Bebas Neue",Impact,sans-serif;font-size:24px;line-height:1;color:var(--navy);box-shadow:0 0 0 4px rgba(255,255,255,.6)}
.big-1{left:220px;width:340px;top:205px;font-size:96px;color:#fff;text-shadow:0 3px 4px rgba(0,0,0,.3)}
.big-2{left:200px;width:380px;top:280px;font-size:104px;color:var(--navy);letter-spacing:-1px;text-shadow:0 3px 3px rgba(0,0,0,.25)}
.amp{color:var(--lime)}
.mission{left:206px;width:340px;top:364px;font-size:11px;line-height:12.6px;color:var(--navy);text-align:center;white-space:nowrap}
.member-box{left:217px;top:420px;width:308px;height:73px;border:1px dotted var(--navy);text-align:center;padding-top:5px}
.member-box h3{font-family:"Bebas Neue",Impact,sans-serif;font-weight:400;font-size:19px;color:var(--ink);line-height:1}
.member-box p{font-size:11px;line-height:1.2;color:var(--navy);margin-top:3px}
.web-bar{left:189px;top:507px;width:370px;height:30px;border-radius:14px 0 0 0;display:flex;align-items:center;justify-content:center;font-weight:700;font-size:16px;letter-spacing:4px}
.front .web-bar{background:var(--paper);color:var(--ink);box-shadow:0 -2px 4px rgba(0,0,0,.15)}
.back .web-bar{background:var(--red);color:#fff}
.elig{left:14px;top:330px;width:185px;height:206px;background:linear-gradient(180deg,var(--navy) 0%,var(--navy) 45%,#8ea0cf 100%);border-radius:8px 8px 0 0;color:#fff;padding:10px 8px 0 16px}
.elig h4{font-size:16px;font-weight:700;line-height:1.05;margin-bottom:2px}
.elig h4.second{margin-top:7px;font-size:14px;margin-left:-2px}
.elig ul{list-style:none}
.elig li{font-size:8.5px;line-height:1.2;position:relative;padding-left:10px;margin-top:1px}
.elig .dis li{margin-top:5px}
.elig li::before{content:"";position:absolute;left:0;top:3px;width:4px;height:4px;border-radius:50%;background:#fff}
.tab{left:559px;top:397px;width:192px;height:40px;background:var(--navy);color:#fff;font-weight:700;font-size:14px;padding:8px 0 0 22px;clip-path:polygon(0 10%,100% 0,100% 100%,6% 100%)}
.back .tab{background:var(--grey-tab);top:392px;height:34px;clip-path:polygon(0 25%,100% 0,100% 100%,3% 100%);padding-top:11px}
.contact-panel{left:541px;top:437px;width:210px;height:99px;padding:10px 0 0 36px;clip-path:polygon(4% 0,100% 0,100% 100%,16% 100%)}
.front .contact-panel{background:var(--mist)}
.back .contact-panel{background:var(--navy);top:426px;height:110px;padding-top:14px;clip-path:polygon(0 0,100% 0,100% 100%,8% 100%)}
.contact-row{display:flex;align-items:center;gap:10px;font-family:"Bebas Neue",Impact,sans-serif;line-height:.95;margin-bottom:7px}
.front .contact-row{color:var(--navy)}
.back .contact-row{color:#fff}
.contact-row svg{flex:none}
.contact-row .phone{font-size:23px}
.contact-row .addr{font-size:12px}
.contact-row .mail{font-size:12.5px}
.how{left:30px;width:150px;top:336px;font-size:34px;color:var(--navy)}
.give{left:17px;width:176px;top:377px;text-align:center;font-weight:700;font-size:15px;line-height:1.17;white-space:nowrap}
.donate-btn{left:54px;top:459px;width:94px;height:26px;border-radius:13px;background:linear-gradient(#ffd86a,#f5a623);border:1px solid #d58a12;text-align:center;font-weight:700;font-size:12px;color:var(--navy);line-height:24px}
.pay-row{left:55px;top:491px;display:flex;gap:3px}
.pay-row span{display:block;width:21px;height:14px;border-radius:2px;background:#cfd6e6;border:1px solid #9aa6c2}
.fine{left:204px;width:328px;text-align:center;font-size:7.6px;line-height:9.6px;color:var(--ink);white-space:nowrap}
.fine strong{font-weight:700}
</style>
</head>
<body>

<div class="side-label front">FRONT</div>
<div class="side-label back">BACK</div>

<!-- Front side: recruitment -->
<section class="card front">
  <h1 class="abs headline top-title">Become a member of our team</h1>

  <svg class="abs band" viewBox="0 0 751 230" aria-hidden="true">
    <defs>
      <linearGradient id="navyBand" x1="0" y1="0" x2="1" y2="0">
        <stop offset="0" stop-color="#142e7a"/>
        <stop offset=".55" stop-color="#2b4fb0"/>
        <stop offset="1" stop-color="#1b3888"/>
      </linearGradient>
    </defs>
    <path d="M0 40 Q380 -5 751 20 L751 230 L0 230 Z" fill="url(#navyBand)"/>
    <path d="M0 40 Q380 -5 751 20" fill="none" stroke="#8aa0d8" stroke-width="3" opacity=".6"/>
  </svg>

  <div class="photo" role="img" aria-label="Photo of a rescuer in helmet, wetsuit and life vest" style="left:12px;top:59px;width:223px;height:270px;background:linear-gradient(160deg,#9a4b46 0%,#6b1f24 45%,#1c1c22 100%);border-radius:40% 40% 8px 8px;opacity:.9"></div>

  <div class="abs badge-seal">KESTREL-SAR</div>

  <div class="photo" role="img" aria-label="White silhouette of a rappelling rescuer on a rope" style="left:492px;top:60px;width:74px;height:180px;background:linear-gradient(180deg,rgba(255,255,255,.1),rgba(255,255,255,.55));border-radius:20px"></div>

  <div class="photo" role="img" aria-label="Photo of a rescue truck towing an inflatable boat" style="left:563px;top:33px;width:188px;height:188px;border-radius:50%;background:linear-gradient(160deg,#c9d4e2,#5b6470 60%,#c53a3a);border:5px solid #fff;box-shadow:0 0 0 2px #dfe4ee"></div>
  <div class="photo" role="img" aria-label="Photo of rescue gear bag" style="left:549px;top:217px;width:144px;height:144px;border-radius:50%;background:linear-gradient(150deg,#5a6b4a,#a3262a 55%,#3b1a1a);border:5px solid #fff;box-shadow:0 0 0 2px #dfe4ee"></div>
  <div class="photo" role="img" aria-label="Photo of a rescue utility vehicle" style="left:657px;top:214px;width:86px;height:86px;border-radius:50%;background:linear-gradient(160deg,#d8dbe0,#7a7f86);border:4px solid #fff"></div>

  <div class="abs headline big-1">Help us</div>
  <div class="abs headline big-2">Save lives</div>

  <p class="abs mission">We are a nonprofit SEARCH and RESCUE team based outside<br>the MARYLAND area. We deploy across the country<br>to help with search and rescue, incident response<br>and disaster relief.</p>

  <div class="abs member-box">
    <h3>KESTREL-SAR Membership</h3>
    <p>is open to volunteers of many disciplines from rescuers or dispatchers to administrators or public affairs, everyone has the opportunity to contribute.</p>
  </div>

  <div class="abs elig">
    <h4>ELIGIBILITY</h4>
    <ul>
      <li>Must be a US citizen or legal resident</li>
      <li>Must be at least 18 years of age</li>
      <li>Must have no disqualifying offenses</li>
    </ul>
    <h4 class="second">DISQUALIFYING ATTRIBUTES INCLUDE:</h4>
    <ul class="dis">
      <li>Military discharge of less then Honorable Discharge</li>
      <li>A criminal history that indicates you have been convicted of a felony offense</li>
      <li>Registered sex offender</li>
    </ul>
  </div>

  <div class="abs tab">Contact Us:</div>
  <div class="abs contact-panel">
    <div class="contact-row">
      <svg width="22" height="22" viewBox="0 0 24 24"><circle cx="12" cy="12" r="10.5" fill="none" stroke="currentColor" stroke-width="2"/><path d="M8.5 6.5l2 2-1.2 1.6c.8 1.7 1.9 2.8 3.6 3.6l1.6-1.2 2 2-1.4 1.8c-3.8-.4-7.6-4.2-8-8z" fill="currentColor"/></svg>
      <span class="phone">555-010-7890</span>
    </div>
    <div class="contact-row">
      <svg width="22" height="22" viewBox="0 0 24 24"><path d="M12 2a7 7 0 0 0-7 7c0 5 7 13 7 13s7-8 7-13a7 7 0 0 0-7-7zm0 9.5a2.5 2.5 0 1 1 0-5 2.5 2.5 0 0 1 0 5z" fill="currentColor"/></svg>
      <span class="addr">210 Harbor Loop Street<br>Dunmore, MD 21090</span>
    </div>
    <div class="contact-row">
      <svg width="22" height="16" viewBox="0 0 24 17"><rect x="1" y="1" width="22" height="15" fill="currentColor"/><path d="M1 1l11 8 11-8" fill="none" stroke="#fff" stroke-width="1.6"/></svg>
      <span class="mail">ops@kestrel-sar.org</span>
    </div>
  </div>

  <div class="abs web-bar">www.kestrel-sar.org</div>
</section>

<!-- Back side: donations -->
<section class="card back">
  <h1 class="abs headline top-title">Support our cause</h1>

  <svg class="abs band" viewBox="0 0 751 230" aria-hidden="true">
    <defs>
      <linearGradient id="redBand" x1="0" y1="0" x2="1" y2="0">
        <stop offset="0" stop-color="#b3121a"/>
        <stop offset=".5" stop-color="#d8262b"/>
        <stop offset="1" stop-color="#b01219"/>
      </linearGradient>
    </defs>
    <path d="M0 30 Q380 -5 751 12 L751 230 L0 230 Z" fill="url(#redBand)"/>
    <path d="M0 30 Q380 -5 751 12" fill="none" stroke="#f3a0a0" stroke-width="3" opacity=".6"/>
  </svg>
  <div class="abs" style="left:0;top:282px;width:751px;height:90px;background:linear-gradient(#e3e4e8,#fff)"></div>

  <div class="abs badge-seal">KESTREL-SAR</div>

  <div class="photo" role="img" aria-label="White silhouette of a rappelling rescuer on a rope" style="left:610px;top:75px;width:110px;height:200px;background:linear-gradient(180deg,rgba(255,255,255,.1),rgba(255,255,255,.6));border-radius:24px"></div>

  <div class="abs" role="img" aria-label="Partner listing badge" style="left:49px;top:206px;width:116px;height:116px;border-radius:50%;background:radial-gradient(circle,#f5b731 0 45%,#1f3d8c 46% 100%);border:4px solid #fff;box-shadow:0 0 0 2px #1f3d8c"></div>

  <div class="abs headline big-1">Donate <span class="amp">&amp;</span></div>
  <div class="abs headline big-2">Save lives</div>

  <div class="photo" role="img" aria-label="Navy silhouette of a rescue helicopter" style="left:595px;top:321px;width:130px;height:54px;background:linear-gradient(90deg,rgba(21,48,122,.85),rgba(21,48,122,.35));border-radius:30px 6px 6px 30px"></div>

  <div class="abs headline how">How Donate</div>
  <p class="abs give">Give Back Donate<br>to KESTREL-SAR<br>Search Rescue<br>and Relief</p>
  <div class="abs donate-btn">QuickGive</div>
  <div class="abs pay-row" aria-label="Accepted payment cards"><span></span><span></span><span></span><span></span></div>

  <p class="abs mission">We are a nonprofit SEARCH and RESCUE team based outside<br>the MARYLAND area. We deploy across the country<br>to help with search and rescue, incident response<br>and disaster relief.</p>
  <p class="abs fine" style="top:421px">We appreciate the support you give us throughout the year and allow us to keep our<br>work platform active, which allows us to keep our human team and rescue tools active<br>and stable in any area where we are required.</p>
  <p class="abs fine" style="top:461px">Visit our Website and learn more details<br>Or take our contact number and request more information.</p>
  <p class="abs fine" style="top:490px"><strong>Thanks for your support!</strong></p>

  <div class="abs tab">Get in touch!</div>
  <div class="abs contact-panel">
    <div class="contact-row">
      <svg width="22" height="22" viewBox="0 0 24 24"><circle cx="12" cy="12" r="10.5" fill="none" stroke="currentColor" stroke-width="2"/><path d="M8.5 6.5l2 2-1.2 1.6c.8 1.7 1.9 2.8 3.6 3.6l1.6-1.2 2 2-1.4 1.8c-3.8-.4-7.6-4.2-8-8z" fill="currentColor"/></svg>
      <span class="phone">555-014-5905</span>
    </div>
    <div class="contact-row">
      <svg width="22" height="22" viewBox="0 0 24 24"><path d="M12 2a7 7 0 0 0-7 7c0 5 7 13 7 13s7-8 7-13a7 7 0 0 0-7-7zm0 9.5a2.5 2.5 0 1 1 0-5 2.5 2.5 0 0 1 0 5z" fill="currentColor"/></svg>
      <span class="addr">210 Harbor Loop Street<br>Dunmore, MD 21090</span>
    </div>
    <div class="contact-row">
      <svg width="22" height="16" viewBox="0 0 24 17"><rect x="1" y="1" width="22" height="15" fill="currentColor"/><path d="M1 1l11 8 11-8" fill="none" stroke="#15307a" stroke-width="1.6"/></svg>
      <span class="mail">ops@kestrel-sar.org</span>
    </div>
  </div>

  <div class="abs web-bar">www.kestrel-sar.org</div>
</section>

</body>
</html>
```